22nd Annual Westbrook Open Cinema Showcase POSTER

Need a modern stylish chic poster for WBOCS's 22nd film festival. Must appeal to our upscale audience and interest new attendees.
Dates are August 23 - 30th, 2019 www.wbocs-example.org

Target Market(s)

we demo flyer attached

Industry/Entity Type

Film Production

Colors

Designer to choose colors to be used in the design.

Requirements
Must have
• Modern, chic, stylish - EYE catching
Nice to have
• Obscure - different - something new
Should not have
• NO CLIP ART

```html
<!DOCTYPE html>
<html lang="en">
<head>
<meta charset="utf-8">
<title>22nd Westbrook Open Cinema Showcase</title>
<link rel="stylesheet" href="https://fonts.googleapis.com/css2?family=Inter:wght@500;700;800;900&family=Playfair+Display:wght@700&display=swap">
<style>
  :root {
    --electric-blue: #0a0de8;
    --poster-black: #121212;
    --ink-white: #f4f4f4;
    --photo-violet: #5b2fd6;
    --photo-magenta: #9a3fd8;
    --photo-deep: #2a1a9a;
  }
  html, body {
    margin: 0;
    padding: 0;
    width: 1200px;
    height: 1000px;
    overflow: hidden;
    background: var(--electric-blue);
  }
  .stage { display: block; width: 1200px; height: 1000px; }
  .poster-sheet { fill: var(--poster-black); }
  .date-month { font-family: "Inter", sans-serif; font-weight: 800; font-size: 29px; fill: var(--ink-white); }
  .date-detail { font-family: "Inter", sans-serif; font-weight: 700; font-size: 20px; fill: var(--ink-white); }
  .festival-title { font-family: "Inter", sans-serif; font-weight: 800; font-size: 84px; fill: var(--ink-white); letter-spacing: 1px; }
  .edition-number { font-family: "Playfair Display", serif; font-weight: 700; font-size: 112px; fill: var(--electric-blue); }
  .edition-ring { font-family: "Inter", sans-serif; font-weight: 500; font-size: 15px; fill: var(--electric-blue); letter-spacing: 1px; }
  .web-ring { font-family: "Inter", sans-serif; font-weight: 700; font-size: 11px; fill: var(--ink-white); letter-spacing: 2px; }
  .brand-name { font-family: "Inter", sans-serif; font-weight: 800; font-size: 22px; fill: var(--ink-white); }
  .brand-tagline { font-family: "Inter", sans-serif; font-weight: 700; font-size: 6.5px; fill: var(--ink-white); }
  .brand-dot { fill: none; stroke: var(--ink-white); stroke-width: 2; }
</style>
</head>
<body>
<svg class="stage" viewBox="0 0 1200 1000" xmlns="http://www.w3.org/2000/svg">
  <defs>
    <linearGradient id="bust-photo-tone" x1="0" y1="0" x2="0.3" y2="1">
      <stop offset="0" stop-color="var(--photo-deep)"/>
      <stop offset="0.45" stop-color="var(--photo-magenta)"/>
      <stop offset="0.8" stop-color="var(--photo-violet)"/>
      <stop offset="1" stop-color="#c9b8f4"/>
    </linearGradient>
    <path id="edition-ring-path" d="M668,265 m-104,0 a104,104 0 1,1 208,0 a104,104 0 1,1 -208,0"/>
    <path id="web-ring-path" d="M362,817 m-34,0 a34,34 0 1,0 68,0 a34,34 0 1,0 -68,0"/>
  </defs>

  <rect class="poster-sheet" x="276" y="106" width="600" height="770"/>

  <g class="event-dates">
    <text class="date-month" x="316" y="165">AUGUST</text>
    <text class="date-detail" x="316" y="194">23th . 30th</text>
    <text class="date-detail" x="316" y="219">2019</text>
  </g>

  <rect class="feature-photo" x="318" y="278" width="292" height="425" fill="url(#bust-photo-tone)"
        role="img" aria-label="Classical marble bust wearing 3D glasses, lit in violet and magenta"/>

  <g class="edition-badge">
    <text class="edition-ring">
      <textPath href="#edition-ring-path" startOffset="0" textLength="640">22ND ANNUAL WESTBROOK OPEN CINEMA SHOWCASE ·</textPath>
    </text>
    <text class="edition-number" x="672" y="292" text-anchor="middle">22</text>
  </g>

  <g class="festival-title-block">
    <text class="festival-title" transform="translate(712,840) rotate(-90)" textLength="385" lengthAdjust="spacingAndGlyphs">WESTBROOK</text>
    <text class="festival-title" transform="translate(778,840) rotate(-90)" textLength="570" lengthAdjust="spacingAndGlyphs">OPEN CINEMA</text>
    <text class="festival-title" transform="translate(845,840) rotate(-90)" textLength="570" lengthAdjust="spacingAndGlyphs">SHOWCASE</text>
  </g>

  <g class="web-address">
    <text class="web-ring">
      <textPath href="#web-ring-path" textLength="205">WWW.WBOCS-EXAMPLE.ORG</textPath>
    </text>
  </g>

  <g class="organiser-mark">
    <circle class="brand-dot" cx="529" cy="792" r="10"/>
    <text class="brand-name" x="529" y="825" text-anchor="middle">WBOCS</text>
    <text class="brand-tagline" x="529" y="836" text-anchor="middle">WESTBROOK OPEN CINEMA SHOWCASE</text>
  </g>
</svg>
</body>
</html>
```